Garden Design Flier

I would like a PDF of this half page A4 flier in soft green tones with dark green leaves.

Target Market(s)

Home owners and real estate agents

Font styles to use
Serif
Other font styles liked:
• Papyrus

Colors
acd136
9bcb3c
cadf82
fefdec

Requirements
Must have
• Green tones
Nice to have
• Leaves, vines, lawns
Should not have
• Open to ideas, but classic style

```html
<!DOCTYPE html>
<html lang="en">
<head>
<meta charset="utf-8">
<title>Verdant Row Gardens – Flier</title>
<link rel="stylesheet" href="https://fonts.googleapis.com/css2?family=Federo&family=Ubuntu:wght@500;700&display=swap">
<style>
  :root {
    --stage: #5a5a5a;
    --white: #ffffff;
    --mint: #5fd39a;
    --mint-light: #7ee3a6;
    --teal: #2fa98a;
    --teal-deep: #1c6b5f;
    --ink: #17544c;
    --ring: #3fcb92;
    --label: #3cc48e;
  }
  * { box-sizing: border-box; margin: 0; padding: 0; }
  html, body { width: 1200px; height: 1200px; overflow: hidden; }
  body { background: var(--stage); position: relative; font-family: "Ubuntu", sans-serif; }

  .flier {
    position: absolute; left: 40px; top: 205px;
    width: 1120px; height: 790px;
    background: var(--white); overflow: hidden;
  }
  .flier__backdrop { position: absolute; inset: 0; width: 100%; height: 100%; }

  .brand-name {
    position: absolute; left: 0; right: 0; top: 26px;
    text-align: center; font-family: "Federo", serif;
    font-size: 78px; color: var(--white); letter-spacing: 1px; line-height: 1;
  }
  .owner-tag {
    position: absolute; left: 423px; top: 145px; width: 280px; height: 34px;
    background: var(--teal-deep); border: 2px solid #9fe6c4; border-radius: 12px;
    color: var(--white); font-weight: 700; font-size: 18px;
    display: flex; align-items: center; justify-content: center;
  }
  .credential {
    position: absolute; left: 0; right: 0; top: 186px; text-align: center;
    font-weight: 700; font-size: 15px; color: var(--ink);
  }

  .services { position: absolute; left: 0; top: 238px; width: 100%; height: 170px; }
  .service { position: absolute; width: 190px; margin-left: -95px; text-align: center; }
  .service__badge {
    width: 118px; height: 118px; margin: 0 auto; border-radius: 50%;
    border: 7px solid var(--ring); background: var(--white);
    display: flex; align-items: center; justify-content: center;
  }
  .service__icon {
    width: 84px; height: 84px; border-radius: 50%;
    background: radial-gradient(circle at 50% 40%, #ffffff 0%, #eef2f1 70%, #dfe6e4 100%);
    box-shadow: 0 3px 6px rgba(0,0,0,.18);
  }
  .service__label {
    margin-top: 12px; font-family: "Federo", serif; font-size: 40px;
    color: var(--label); line-height: 1;
  }

  .pitch {
    position: absolute; left: 0; right: 0; top: 422px; text-align: center;
    font-weight: 500; font-size: 21px; line-height: 29px; color: var(--ink);
  }

  .branch-art {
    position: absolute; left: 40px; top: 570px; width: 580px; height: 210px;
    border-radius: 50%;
    background: radial-gradient(ellipse at 45% 45%, rgba(126,227,166,.75) 0%, rgba(95,211,154,.35) 55%, rgba(95,211,154,0) 75%);
  }

  .contact {
    position: absolute; left: 700px; top: 592px; width: 340px; text-align: center;
    color: var(--white); font-weight: 700; font-size: 18px;
  }
  .contact__icon {
    width: 32px; height: 32px; margin: 0 auto 8px; border-radius: 50%;
    background: var(--teal-deep); border: 2px solid #bdeed7;
    display: flex; align-items: center; justify-content: center;
  }
  .contact__line { margin-bottom: 18px; }
  .contact__line--abn { color: var(--ink); margin-top: -2px; }
</style>
</head>
<body>
  <main class="flier">
    <svg class="flier__backdrop" viewBox="0 0 1120 790" aria-hidden="true">
      <defs>
        <linearGradient id="topBand" x1="0" y1="0" x2="1" y2="1">
          <stop offset="0" stop-color="#3bb394"/>
          <stop offset="1" stop-color="#62d69a"/>
        </linearGradient>
        <linearGradient id="bottomField" x1="0" y1="0" x2="1" y2="1">
          <stop offset="0" stop-color="#6adf9c"/>
          <stop offset="0.55" stop-color="#45c392"/>
          <stop offset="1" stop-color="#2a9f86"/>
        </linearGradient>
        <linearGradient id="lightBand" x1="0" y1="0" x2="1" y2="0">
          <stop offset="0" stop-color="#7ee3a6"/>
          <stop offset="1" stop-color="#58cf97"/>
        </linearGradient>
      </defs>
      <!-- header band -->
      <path d="M0,0 H1120 V118 C930,150 700,170 500,150 C300,130 140,80 0,36 Z" fill="url(#topBand)"/>
      <path d="M780,176 C900,168 1020,150 1120,122 V134 C1020,160 900,178 780,176 Z" fill="var(--teal-deep)"/>
      <!-- footer waves -->
      <path d="M0,508 C160,530 330,575 520,585 C700,595 900,640 1120,640 V790 H0 Z" fill="url(#bottomField)"/>
      <path d="M0,530 C200,560 380,600 560,600 C760,600 900,560 1120,590 V640 C920,610 760,640 560,630 C360,620 180,575 0,560 Z" fill="url(#lightBand)"/>
      <path d="M28,506 C180,520 360,545 523,548 C360,552 170,540 28,506 Z" fill="var(--teal-deep)"/>
      <path d="M560,610 C760,585 940,575 1120,612 V652 C950,620 770,625 560,610 Z" fill="var(--teal-deep)"/>
    </svg>

    <h1 class="brand-name">Verdant Row Gardens</h1>
    <p class="owner-tag">By Reid Calloway</p>
    <p class="credential">Certificate 3.&nbsp; Horticulture Regional College</p>

    <section class="services">
      <div class="service" style="left:190px">
        <div class="service__badge"><div class="service__icon" role="img" aria-label="Four-leaf design icon"></div></div>
        <p class="service__label">Design</p>
      </div>
      <div class="service" style="left:378px">
        <div class="service__badge"><div class="service__icon" role="img" aria-label="Seedling and trowel icon"></div></div>
        <p class="service__label">Install</p>
      </div>
      <div class="service" style="left:563px">
        <div class="service__badge"><div class="service__icon" role="img" aria-label="Sprout icon"></div></div>
        <p class="service__label">Grow</p>
      </div>
      <div class="service" style="left:749px">
        <div class="service__badge"><div class="service__icon" role="img" aria-label="Pruning shears icon"></div></div>
        <p class="service__label">Tend</p>
      </div>
      <div class="service" style="left:936px">
        <div class="service__badge"><div class="service__icon" role="img" aria-label="Flower with butterflies icon"></div></div>
        <p class="service__label">Enjoy</p>
      </div>
    </section>

    <p class="pitch">All your gardening and landscaping needs from design &amp; installation to general maintenance<br>Bespoke vegetable gardens and potager designs created to suite your site and requirements.</p>

    <div class="branch-art" role="img" aria-label="Illustrated branch with green leaves"></div>

    <address class="contact" style="font-style:normal">
      <div class="contact__icon">
        <svg width="16" height="12" viewBox="0 0 16 12" aria-hidden="true"><rect x="1" y="1" width="14" height="10" rx="1" fill="none" stroke="#fff" stroke-width="1.5"/><path d="M1.5,1.5 L8,7 L14.5,1.5" fill="none" stroke="#fff" stroke-width="1.5"/></svg>
      </div>
      <p class="contact__line">reid@verdantrowgardens.com.au</p>
      <div class="contact__icon">
        <svg width="16" height="16" viewBox="0 0 24 24" aria-hidden="true"><path d="M6.6 10.8a15.1 15.1 0 0 0 6.6 6.6l2.2-2.2a1 1 0 0 1 1-.25 11.4 11.4 0 0 0 3.6.57 1 1 0 0 1 1 1V20a1 1 0 0 1-1 1A17 17 0 0 1 3 4a1 1 0 0 1 1-1h3.5a1 1 0 0 1 1 1c0 1.25.2 2.45.57 3.57a1 1 0 0 1-.25 1z" fill="#fff"/></svg>
      </div>
      <p class="contact__line">0491-570 118</p>
      <p class="contact__line contact__line--abn">ABN: 51824753556</p>
    </address>
  </main>
</body>
</html>
```